NORVANTEC IT SUPPORT WEBSITE AND CODING

We are a small IT Support company based if Broome Western Australia, we need to have our existing website www.norvantec.com.au converted or redesigned to a format that can be read on iphone , ipad and all browsers, must have facebook like button.

THIS PROJECT IS FOR DESIGN AND CODING OF COMPLETE WEBSITE.
Updates

Target Market(s)

Broome Local Businesses and Public.

Industry/Entity Type

It Company

Requirements
Must have
• Must be able to be viewed on all mobile devices , iphone , ipad , must have a facebook like button, the logo for norvanTEC is the way norvan tec is written in orange on the current website which is used on all our advertising which needs to stay the same or only change slightly.
Nice to have
• Contact us page that emails us.
Our address on a map.

```html
<!DOCTYPE html>
<html lang="en">
<head>
<meta charset="utf-8">
<title>norvanTEC – IT Support</title>
<link rel="stylesheet" href="https://fonts.googleapis.com/css2?family=Barlow:wght@300;400;500;600;700&family=Gelasio:ital@1&family=Arimo:wght@400;700&display=swap">
<style>
:root{
  --orange:#e8621f;
  --orange-light:#f0813b;
  --orange-dark:#c94d14;
  --accent:#f07a1c;
  --slate:#4e5d6b;
  --slate-dark:#323c46;
  --footer:#4a5866;
  --ink:#2b2b2b;
  --muted:#555;
  --rule:#d6d9dc;
  --white:#fff;
}
*{box-sizing:border-box;margin:0;padding:0}
html,body{width:1200px;height:891px;overflow:hidden}
body{position:relative;background:var(--white);font-family:"Arimo",Arial,sans-serif;color:var(--ink)}
.abs{position:absolute}

/* header */
.logo{left:232px;top:22px;font-family:"Barlow",sans-serif;font-weight:400;font-size:34px;color:var(--orange);letter-spacing:-.5px}
.like{left:712px;top:34px;display:flex;gap:6px;align-items:center;font-size:10px}
.like-btn{border:1px solid #9fb0cf;background:#eef2f8;color:#3b5998;padding:2px 5px;font-weight:700;border-radius:2px}
.like-count{border:1px solid #c2c9d6;padding:2px 6px;color:#333;background:#fff;border-radius:2px}
.support{left:801px;top:26px;width:173px;height:34px;border:1px solid #cfcfcf;border-radius:3px;background:linear-gradient(#fff,#f1f1f1);box-shadow:0 1px 2px rgba(0,0,0,.12);font-family:"Barlow",sans-serif;font-size:12px;letter-spacing:.3px;color:#666;display:flex;align-items:center;justify-content:center}

/* nav */
.nav{left:0;top:84px;width:1200px;height:46px;background:linear-gradient(var(--orange-light),var(--orange) 55%,var(--orange-dark))}
.nav ul{list-style:none;position:absolute;left:232px;top:0;display:flex;height:46px;border-right:1px solid #b8480f}
.nav li{width:150px;height:46px;display:flex;align-items:center;justify-content:center;font-family:"Barlow",sans-serif;font-size:14px;color:var(--white);border-left:1px solid #b8480f;letter-spacing:.3px}
.nav li.active{background:linear-gradient(#5d6c7a,var(--slate));font-weight:600;width:148px;border-left:none}

/* hero */
.hero{left:0;top:130px;width:1200px;height:252px;background:radial-gradient(ellipse at 55% 60%,#8a6a4a 0%,#4a3a2e 40%,#1e1a18 100%)}
.hero-title{left:230px;top:176px;font-family:"Barlow",sans-serif;font-weight:300;font-size:38px;line-height:48px;color:var(--white);text-shadow:0 2px 3px rgba(0,0,0,.5)}
.hero-title b{font-weight:600}
.btn{top:301px;width:180px;height:38px;border-radius:2px;font-family:"Barlow",sans-serif;font-weight:700;font-size:17px;display:flex;align-items:center;gap:10px;padding-left:14px;box-shadow:0 2px 3px rgba(0,0,0,.35)}
.btn-learn{left:231px;background:linear-gradient(#ffb21e,#f08a00);color:#5a2e00}
.btn-contact{left:426px;background:linear-gradient(#fafafa,#cfcfcf);color:#2a2a2a}
.hero-art{left:695px;top:160px;width:265px;height:250px;border-radius:6px;background:linear-gradient(135deg,#d0322b 0%,#a51f1a 45%,#8a9aa8 70%,#c9ced2 100%)}

/* content */
.content-bg{left:0;top:382px;width:1200px;height:120px;background:linear-gradient(#eef5f9,#fff)}
.heading{font-family:"Barlow",sans-serif;font-weight:400;font-size:22px;color:#2a2a2a;letter-spacing:.3px;padding-bottom:5px;border-bottom:1px solid var(--rule)}
.heading b{color:var(--accent);font-weight:600}
.intro{left:232px;top:478px;width:350px;font-family:"Gelasio",Georgia,serif;font-style:italic;font-size:12px;line-height:19.6px;color:#444}
.badge{left:619px;top:478px;width:90px;height:90px;border:1px solid #ddd;background:#fff;box-shadow:0 1px 2px rgba(0,0,0,.08)}
.small{font-size:10px;line-height:16.5px;color:#333}
.btn-sm{border:1px solid #c6c6c6;border-radius:3px;background:linear-gradient(#fff,#ececec);display:flex;align-items:center;gap:6px;color:#333}
.dot{width:10px;height:10px;border-radius:50%;background:#b5b5b5;display:inline-block}
.avatar{width:67px;height:58px;border:1px solid #ddd;padding:3px;background:#fff}
.avatar span{display:block;width:100%;height:100%;background:linear-gradient(#d8cfc6,#a8917f)}
.by{font-size:10px;color:#777}
.by b{color:#555}
.divider{height:1px;background:#eee}

/* footer */
.footer{left:0;top:821px;width:1200px;height:70px;background:var(--footer);border-top:3px solid var(--slate-dark)}
.foot-links{left:231px;top:855px;display:flex;font-size:9px;color:#fff}
.foot-links span{margin-right:12px}
.foot-links i{font-style:normal;margin-right:12px;color:#c5ccd3}
.copy{left:618px;top:855px;font-size:9px;color:#dde2e6}
.follow{left:855px;top:848px;display:flex;align-items:center;gap:8px;font-size:9px;font-weight:700;color:#fff}
.sq{width:22px;height:22px;border-radius:3px}
</style>
</head>
<body>
<header>
  <div class="abs logo">norvanTEC</div>
  <div class="abs like"><span class="like-btn">Like</span><span class="like-count">303</span></div>
  <div class="abs support">GREAT CUSTOMERS SUPPORT</div>
</header>

<nav class="abs nav">
  <ul>
    <li class="active">HOME</li><li>ABOUT US</li><li>SERVICES</li><li>OUR PRICES</li><li>CONTACT US</li>
  </ul>
</nav>

<section>
  <div class="abs hero" role="img" aria-label="Blurred photo of a busy computer workshop"></div>
  <h1 class="abs hero-title">The experince <b>you Need</b><br>&amp; Quality <b>you Deserve</b></h1>
  <div class="abs btn btn-learn"><svg width="20" height="12" viewBox="0 0 20 12"><path d="M1 6h12M9 2l4 4-4 4M7 2l4 4-4 4" stroke="#5a2e00" stroke-width="2" fill="none"/></svg>LEARN MORE</div>
  <div class="abs btn btn-contact"><svg width="20" height="12" viewBox="0 0 20 12"><path d="M1 6h12M9 2l4 4-4 4M7 2l4 4-4 4" stroke="#555" stroke-width="2" fill="none"/></svg>CONTACT US</div>
  <div class="abs hero-art" role="img" aria-label="Laptop sheltered by a red umbrella"></div>
</section>

<main>
  <div class="abs content-bg"></div>

  <h2 class="abs heading" style="left:232px;top:428px;width:355px">WELCOME TO <b>OUR SITE</b></h2>
  <p class="abs intro">Lorem ipsum dolor sit amet, consectetur adipiscing elit. In ipsum libero, congue id varius vel, commodo volutpat dolor. Praesent purus nisi, euismod non cursus fermentum, hendrerit quis ante. Integer pulvinar viverra tristique. Vivamus rhoncus feugiat felis id luctus.</p>

  <h2 class="abs heading" style="left:618px;top:428px;width:355px">BEST <b>SERVICE</b></h2>
  <div class="abs badge" role="img" aria-label="Certification badge"></div>
  <p class="abs small" style="left:729px;top:476px;width:245px">Lorem ipsum dolor sit amet, consectetur adipiscing elit. In ipsum libero, congue id varius vel, commodo volutpat dolor. Praesent purus nisi, euismod non ...</p>
  <div class="abs btn-sm" style="left:728px;top:540px;width:90px;height:28px;padding-left:10px;font-size:10px;font-weight:700">Learn More <span class="dot"></span></div>

  <h2 class="abs heading" style="left:232px;top:596px;width:355px;padding-left:5px">OUR <b>TESTIMONIALS</b></h2>
  <div class="abs avatar" style="left:232px;top:642px"><span role="img" aria-label="Customer portrait"></span></div>
  <p class="abs small" style="left:327px;top:647px;width:240px">Lorem ipsum dolor sit amet,&nbsp; commodo volutpat dolor. Praesent purus nisi, euismod non ...</p>
  <p class="abs by" style="left:327px;top:683px">By: <b>marthon</b></p>
  <div class="abs divider" style="left:232px;top:716px;width:355px"></div>
  <div class="abs avatar" style="left:232px;top:732px"><span role="img" aria-label="Customer portrait"></span></div>
  <p class="abs small" style="left:327px;top:737px;width:240px">Lorem ipsum dolor sit amet,&nbsp; commodo volutpat dolor. Praesent purus nisi, euismod non ...</p>
  <p class="abs by" style="left:327px;top:773px">By: <b>marthon</b></p>

  <h2 class="abs heading" style="left:618px;top:596px;width:355px">LATEST <b>NEWS</b></h2>
  <span class="abs dot" style="left:624px;top:650px;width:12px;height:12px"></span>
  <p class="abs small" style="left:643px;top:647px;width:310px">Lorem ipsum dolor sit amet,&nbsp; commodo volutpat dolor. Praesent purus nisi, euismod non ...</p>
  <div class="abs btn-sm" style="left:643px;top:681px;width:71px;height:20px;padding-left:6px;font-size:8px;color:#777">Learn More <span class="dot"></span></div>
  <div class="abs divider" style="left:618px;top:716px;width:355px"></div>
  <span class="abs dot" style="left:624px;top:730px;width:12px;height:12px"></span>
  <p class="abs small" style="left:643px;top:727px;width:310px">Lorem ipsum dolor sit amet,&nbsp; commodo volutpat dolor. Praesent purus nisi, euismod non ...</p>
  <div class="abs btn-sm" style="left:643px;top:761px;width:71px;height:20px;padding-left:6px;font-size:8px;color:#777">Learn More <span class="dot"></span></div>
</main>

<footer>
  <div class="abs footer"></div>
  <div class="abs foot-links"><span style="font-weight:700">Home</span><i>|</i><span>Privacy Policy</span><i>|</i><span>FAQ's</span><i>|</i><span>Sitemap</span><i>|</i><span>Contact us</span></div>
  <div class="abs copy">All Right Reserved, Norvan Tec</div>
  <div class="abs follow">Follow us on:<span class="sq" style="background:#4a6fb0"></span><span class="sq" style="background:#5bc3e8"></span></div>
</footer>
</body>
</html>
```